Media Banner

Create a banner similar to the one in the link below showing the various media publications (TVQRN, Marlowby Ledger, Kite Wire, Pellanstroud Bulletin) and then link to "More News..."

https://www.loanvistra.com/

The bar on loan vistra is blue. Please make this bar organe to match this site:
www.bramfieldlegal.com
The bar will be used on this cite to run accross the page.

Industry/Entity Type

Graphic Design

```html
<!DOCTYPE html>
<html lang="en">
<head>
<meta charset="utf-8">
<title>Bramfield Firm – Media Banner</title>
<link href="https://fonts.googleapis.com/css2?family=PT+Sans:wght@400;700&display=swap" rel="stylesheet">
<style>
  :root {
    --page-bg: #333333;
    --nav-bg: #343434;
    --surface: #ffffff;
    --column-bg: #f8f8f8;
    --divider: #e6e6e4;
    --ink: #2e2e2e;
    --ink-soft: #8a8a8a;
    --nav-ink: #bdbdbd;
    --nav-active: #ffffff;
    --orange-top: #f78c3e;
    --orange-bottom: #ee7a2c;
    --icon-grey: #d0d0d0;
    --field-border: #cfcfcf;
    --required: #b0121b;
  }
  * { box-sizing: border-box; margin: 0; padding: 0; }
  html, body { width: 1200px; height: 585px; overflow: hidden; }
  body {
    position: relative;
    background: var(--page-bg);
    font-family: "PT Sans", Arial, sans-serif;
    color: var(--ink);
  }
  .abs { position: absolute; }

  /* Header */
  .site-header { left: 120px; top: 0; width: 961px; height: 162px; background: var(--surface); }
  .brand-name { left: 34px; top: 25px; font-size: 33px; letter-spacing: 0.3px; color: var(--ink); font-weight: 400; }
  .brand-tagline { left: 34px; top: 59px; font-size: 12px; color: var(--ink-soft); }
  .header-phone { right: 33px; top: 29px; font-size: 13.5px; font-weight: 700; }
  .header-cta { right: 33px; top: 68px; font-size: 12.5px; }
  .social-row { right: 38px; top: 88px; display: flex; gap: 13px; }
  .social-tile { width: 27px; height: 29px; background: var(--icon-grey); border-radius: 2px; }
  .nav-pointer { left: 151px; top: 162px; width: 0; height: 0;
    border-left: 8px solid transparent; border-right: 8px solid transparent; border-top: 8px solid var(--surface); z-index: 2; }

  /* Navigation */
  .main-nav { left: 120px; top: 162px; width: 961px; height: 109px; background: var(--nav-bg); }
  .nav-link { font-size: 13px; color: var(--nav-ink); text-transform: uppercase; white-space: nowrap; }
  .nav-link.is-active { color: var(--nav-active); }
  .nav-date { right: 24px; top: 22px; font-size: 13px; color: var(--nav-ink); }

  /* Media banner */
  .media-banner { left: 120px; top: 271px; width: 962px; height: 47px;
    background: linear-gradient(to bottom, var(--orange-top), var(--orange-bottom));
    color: #fff; }
  .media-label { left: 11px; top: 16px; font-size: 11.5px; font-weight: 700; letter-spacing: 0.3px; }
  .media-name { top: 50%; transform: translateY(-50%); font-weight: 700; color: #fff; white-space: nowrap; }
  .media-more { left: 818px; top: 17px; font-size: 11px; font-weight: 700; letter-spacing: 0.5px; }

  /* Columns */
  .content-strip { left: 120px; top: 322px; width: 961px; height: 263px; background: var(--divider); }
  .column { top: 0; height: 263px; background: var(--column-bg); text-align: center; }
  .illustration { background: #111; border-radius: 4px; }
  .column-title { position: absolute; left: 0; right: 0; font-size: 20px; font-weight: 400; color: var(--ink); }
  .column-text { position: absolute; left: 0; right: 0; font-size: 12.5px; line-height: 22px; color: var(--ink-soft); }
  .cta-button { background: var(--orange-top); border-radius: 2px; }

  /* Contact form */
  .form-title { left: 0; right: 0; top: 40px; font-size: 13.5px; font-weight: 700; text-align: center; }
  .field-label { font-size: 12.5px; font-weight: 700; text-align: left; }
  .field-label .req { color: var(--required); font-size: 10px; vertical-align: top; margin-left: 2px; }
  .field-input { background: #fff; border: 1px solid var(--field-border); border-radius: 2px; }
  .field-hint { font-size: 12.5px; color: var(--ink); text-align: left; }
</style>
</head>
<body>

<header class="abs site-header">
  <div class="abs brand-name">BRAMFIELD FIRM</div>
  <div class="abs brand-tagline">Employment and Injury Attorneys</div>
  <div class="abs header-phone">555-014-2200</div>
  <div class="abs header-cta">FREE CASE EVALUATION</div>
  <div class="abs social-row" aria-label="Social links">
    <span class="social-tile"></span><span class="social-tile"></span><span class="social-tile"></span><span class="social-tile"></span><span class="social-tile"></span>
  </div>
</header>
<div class="abs nav-pointer"></div>

<nav class="abs main-nav">
  <span class="abs nav-link is-active" style="left:20px;top:22px">Home</span>
  <span class="abs nav-link" style="left:101px;top:22px">Firm</span>
  <span class="abs nav-link" style="left:174px;top:22px">Blog</span>
  <span class="abs nav-link" style="left:249px;top:22px">Press</span>
  <span class="abs nav-link" style="left:331px;top:22px">Client Reviews</span>
  <span class="abs nav-link" style="left:473px;top:22px">Legal Fees</span>
  <span class="abs nav-link" style="left:586px;top:22px">Contact</span>
  <span class="abs nav-date">JANUARY 7, 2014</span>
  <span class="abs nav-link" style="left:20px;top:71px">Employee Rights Guide</span>
  <span class="abs nav-link" style="left:215px;top:71px">Types of Employment Cases</span>
</nav>

<section class="abs media-banner" aria-label="Featured in">
  <span class="abs media-label">Featured in:</span>
  <span class="abs media-name" style="left:125px;font-size:22px;letter-spacing:-0.5px">TVQRN</span>
  <span class="abs media-name" style="left:314px;font-size:10.5px;line-height:11px">Pellanstroud<br>Bulletin</span>
  <span class="abs media-name" style="left:458px;font-size:19px;font-weight:400">MARLOWBY LEDGER</span>
  <span class="abs media-name" style="left:739px;font-size:11px;line-height:11px">KITE<br>WIRE</span>
  <span class="abs media-more">MORE NEWS...</span>
</section>

<main class="abs content-strip">
  <article class="abs column" style="left:0;width:317px">
    <div class="abs illustration" role="img" aria-label="Icon of a person in suit and tie" style="left:112px;top:34px;width:99px;height:114px"></div>
    <h2 class="column-title" style="top:175px">EMPLOYMENT CASES</h2>
    <p class="column-text" style="top:214px">Have you been fired, harassed, cheated out<br>of pay or otherwise kicked around at work?</p>
  </article>

  <article class="abs column" style="left:321px;width:317px">
    <div class="abs illustration" role="img" aria-label="Icon of two cars in a collision" style="left:61px;top:40px;width:202px;height:78px"></div>
    <h2 class="column-title" style="top:134px">PERSONAL INJURY CASES</h2>
    <p class="column-text" style="top:173px">All personal injury cases are handled on a<br>contingent fee basis.&nbsp; Here are the types of<br>cases we ...</p>
    <div class="abs cta-button" style="left:86px;top:255px;width:143px;height:10px"></div>
  </article>

  <aside class="abs column" style="left:641px;width:320px">
    <h3 class="abs form-title">CONTACT US</h3>
    <span class="abs field-label" style="left:34px;top:73px">Name<span class="req">•</span></span>
    <div class="abs field-input" style="left:118px;top:70px;width:74px;height:46px"></div>
    <div class="abs field-input" style="left:199px;top:70px;width:74px;height:46px"></div>
    <span class="abs field-hint" style="left:118px;top:121px">First</span>
    <span class="abs field-hint" style="left:199px;top:121px">Last</span>
    <span class="abs field-label" style="left:34px;top:160px">Email<span class="req">•</span></span>
    <div class="abs field-input" style="left:118px;top:158px;width:86px;height:46px"></div>
    <span class="abs field-label" style="left:34px;top:220px">Number</span>
    <div class="abs field-input" style="left:118px;top:218px;width:86px;height:50px"></div>
  </aside>
</main>

</body>
</html>
```